Award-winnning Estate Agent needs a premium version of their 'For Sale' board design

We need a premium option for our 'For Sale' board design. We have a standard board that is attached to this brief, but were are looking to have a premium design version that we will use when selling exclusive properties. Our company name is Harbour Lane Estates and the name for this is exclusive selection is: 'The Harbour Collection'. The design needs to work with our current brand, but have a distinctive PREMIUM feel to it. I have uploaded the barnd guidelines and also some of the exisisting logo variations. We do NOT need a new logo but feel free to play around with colours, fonts, sizes etc. for the sign.

Target Market(s)

Property buyers & house hunters

Industry/Entity Type

Real Estate - Residential Property

Font styles to use
Sans Serif

Requirements
Must have
• A premium fee, must be square design, must be easy to read when driving past the sign
Nice to have
• I'm open ot ideas

```html
<!DOCTYPE html>
<html lang="en">
<head>
<meta charset="utf-8">
<title>Harbour Lane Estates – The Harbour Collection For Sale Board</title>
<link href="https://fonts.googleapis.com/css2?family=Arimo:wght@400;700&display=swap" rel="stylesheet">
<style>
  :root {
    --brand-navy: #3B4592;
    --brand-deep: #232A63;
    --brand-sky: #00B0F0;
    --accent-gold: #C8A65A;
    --board-white: #FFFFFF;
    --page-bg: #FDFDFD;
  }
  html, body {
    margin: 0;
    padding: 0;
    width: 1200px;
    height: 1200px;
    overflow: hidden;
    background: var(--page-bg);
  }
  .sale-board {
    display: block;
    width: 1200px;
    height: 1200px;
    font-family: "Arimo", Arial, sans-serif;
  }
  .frame-outer { fill: var(--brand-deep); }
  .frame-rule { fill: var(--accent-gold); }
  .panel { fill: var(--board-white); }
  .phone-band { fill: var(--brand-navy); }
  .band-rule { fill: var(--accent-gold); }
  .brand-mark { fill: var(--brand-sky); }
  .divider { stroke: var(--accent-gold); stroke-width: 2; }
  .brand-name {
    fill: var(--brand-navy);
    font-weight: 700;
    font-size: 40px;
  }
  .collection-name {
    fill: var(--accent-gold);
    font-weight: 700;
    font-size: 20px;
    letter-spacing: 6px;
  }
  .headline-small {
    fill: var(--brand-navy);
    font-weight: 400;
    font-size: 54px;
    letter-spacing: 14px;
  }
  .headline-large {
    fill: var(--brand-deep);
    font-weight: 700;
    font-size: 270px;
  }
  .phone-number {
    fill: var(--board-white);
    font-weight: 700;
    font-size: 100px;
  }
  .web-address {
    fill: var(--brand-navy);
    font-weight: 700;
    font-size: 48px;
  }
</style>
</head>
<body>
<svg class="sale-board" viewBox="0 0 1200 1200" xmlns="http://www.w3.org/2000/svg" role="img" aria-label="Harbour Lane Estates, The Harbour Collection, For Sale board">
  <rect class="frame-outer" x="121" y="121" width="966" height="966"/>
  <rect class="frame-rule" x="153" y="153" width="902" height="902"/>
  <rect class="panel" x="159" y="159" width="890" height="890"/>

  <rect class="brand-mark" x="572" y="205" width="56" height="56"/>
  <text class="brand-name" x="600" y="316" text-anchor="middle">Harbour Lane Estates</text>

  <line class="divider" x1="300" y1="352" x2="372" y2="352"/>
  <text class="collection-name" x="603" y="359" text-anchor="middle">THE HARBOUR COLLECTION</text>
  <line class="divider" x1="828" y1="352" x2="900" y2="352"/>

  <text class="headline-small" x="607" y="465" text-anchor="middle">FOR</text>
  <text class="headline-large" x="244" y="735" textLength="719" lengthAdjust="spacingAndGlyphs">SALE</text>

  <rect class="phone-band" x="159" y="790" width="890" height="140"/>
  <rect class="band-rule" x="159" y="790" width="890" height="4"/>
  <rect class="band-rule" x="159" y="926" width="890" height="4"/>
  <text class="phone-number" x="210" y="897" textLength="780" lengthAdjust="spacingAndGlyphs">01632 960123</text>

  <text class="web-address" x="244" y="1003" textLength="719" lengthAdjust="spacingAndGlyphs">www.harbourlaneestates.co.uk</text>
</svg>
</body>
</html>
```